Mosk trail Website

We need a simple web page design for our businessWe procure and dispose of earthmoving construction equipmentwe also find construction equipment for our customers using our global contacts

Number of Pages Required

1 page

```html
<!DOCTYPE html>
<html lang="en">
<head>
<meta charset="utf-8">
<title>Mosk trail – Earthmoving &amp; Civil Works</title>
<link href="https://fonts.googleapis.com/css2?family=Montserrat:wght@600;700;800&family=Raleway:wght@400;500;600;700&display=swap" rel="stylesheet">
<style>
:root{
  --orange:#f04e14;
  --orange-deep:#e2400a;
  --orange-soft:#f7753a;
  --ink:#222;
  --text:#444;
  --muted:#666;
  --white:#fff;
  --paper:#f4f4f4;
  --footer:#2a2a2a;
  --footer-deep:#1d1d1d;
  --footer-text:#bdbdbd;
}
*{margin:0;padding:0;box-sizing:border-box}
html,body{width:1200px;height:2494px;overflow:hidden}
body{position:relative;background:var(--white);font-family:"Raleway",sans-serif;color:var(--text)}
.abs{position:absolute}
h1,h2,h3,h4{font-family:"Montserrat",sans-serif;font-weight:700;color:var(--ink)}

/* header */
.site-header{position:absolute;left:0;top:0;width:1200px;height:94px;background:var(--white)}
.brand{position:absolute;left:136px;top:24px;display:flex;align-items:center;gap:12px}
.brand-mark{width:40px;height:40px;background:var(--orange)}
.brand-name{font-family:"Montserrat",sans-serif;font-weight:700;font-size:30px;color:var(--ink);line-height:1}
.contact-strip{position:absolute;left:662px;top:0;width:538px;height:44px}
.contact-item{position:absolute;top:6px;display:flex;align-items:center;gap:12px;color:var(--white)}
.contact-icon{width:24px;height:24px;border:1.5px solid var(--white);border-radius:50%;display:flex;align-items:center;justify-content:center}
.contact-label{font-size:10px;line-height:12px;opacity:.85}
.contact-value{font-size:13px;font-weight:700;line-height:16px}
.main-nav{position:absolute;top:64px;left:0;font-size:12.5px;font-weight:600;color:var(--ink);text-transform:uppercase}
.main-nav span{position:absolute;white-space:nowrap}

/* hero (children positioned relative to hero) */
.hero{position:absolute;left:0;top:94px;width:1200px;height:492px}
.hero-title{position:absolute;left:136px;top:176px;font-size:29px;line-height:36px;color:var(--white);letter-spacing:.3px;white-space:nowrap}
.hero-text{position:absolute;left:139px;top:222px;width:600px;font-size:12px;line-height:22px;color:var(--white)}
.btn{position:absolute;display:flex;align-items:center;justify-content:center;background:var(--orange);color:var(--white);font-family:"Montserrat",sans-serif;font-weight:700;font-size:11.5px;text-transform:uppercase}
.hero-arrow{position:absolute;top:216px;width:20px;height:20px}

/* services */
.section-title{position:absolute;left:0;width:1200px;text-align:center;font-size:21px;text-transform:uppercase}
.section-title em{font-style:normal;color:var(--orange)}
.service{position:absolute;top:716px;width:240px;text-align:center}
.service-photo{width:206px;height:206px;margin:0 auto;border-radius:50%;border:4px solid #ddd}
.service h3{font-size:13px;margin-top:24px;text-transform:uppercase}
.service p{font-size:11.5px;line-height:19px;margin:8px auto 0;width:190px;color:var(--text)}

/* about */
.about-photo{position:absolute;left:136px;top:1120px;width:369px;height:295px;border-radius:48px;border:3px solid var(--white)}
.about-title{position:absolute;left:561px;top:1134px;font-size:20px;color:var(--white);text-transform:uppercase}
.about-text{position:absolute;left:561px;width:450px;font-size:11.5px;line-height:23px;color:var(--white)}

/* equipment */
.equip{position:absolute;width:296px;text-align:center}
.equip-photo{width:296px;height:169px}
.equip h4{font-size:12px;margin-top:22px;text-transform:uppercase}

/* footer */
.footer-col{position:absolute;top:2201px;color:var(--footer-text);font-size:11.5px}
.footer-col h4{font-size:11px;color:var(--white);text-transform:uppercase;margin-bottom:22px}
.footer-links li{list-style:none;line-height:24px}
.info-row{display:flex;gap:14px;line-height:22px;margin-bottom:14px}
.info-icon{width:13px;flex:none;padding-top:4px}
.newsletter-note{font-size:10.5px;line-height:20px;text-transform:uppercase;width:210px}
.signup{display:flex;margin-top:14px}
.signup-field{width:156px;height:38px;background:var(--white);font-size:10.5px;color:#aaa;padding:12px 10px}
.signup-btn{width:36px;height:38px;background:var(--orange);display:flex;align-items:center;justify-content:center}
.social{display:flex;gap:6px}
.social span{width:31px;height:25px;background:#4a4a4a;display:block}
.copyright{position:absolute;left:0;top:2448px;width:1200px;height:46px;background:var(--footer-deep);color:#9a9a9a;font-size:10px;padding:16px 0 0 141px}
</style>
</head>
<body>

<header class="site-header">
  <div class="brand"><span class="brand-mark"></span><span class="brand-name">Mosk trail</span></div>
  <svg class="contact-strip" viewBox="0 0 538 44" aria-hidden="true"><polygon points="0,0 538,0 538,44 22,44" fill="var(--orange)"/></svg>
  <div class="contact-item" style="left:722px">
    <span class="contact-icon"><svg width="12" height="9" viewBox="0 0 12 9"><rect x=".6" y=".6" width="10.8" height="7.8" fill="none" stroke="#fff" stroke-width="1.2"/><path d="M.6 .6 6 5 11.4 .6" fill="none" stroke="#fff" stroke-width="1.2"/></svg></span>
    <div><div class="contact-label">email us</div><div class="contact-value">hello@mosktrail.example</div></div>
  </div>
  <div class="contact-item" style="left:944px">
    <span class="contact-icon"><svg width="11" height="11" viewBox="0 0 12 12"><path d="M2 1l2.2 0 1 3-1.4 1a7 7 0 0 0 3.2 3.2l1-1.4 3 1V10a1 1 0 0 1-1 1A9 9 0 0 1 1 2a1 1 0 0 1 1-1z" fill="#fff"/></svg></span>
    <div><div class="contact-label">call now</div><div class="contact-value">0400 123 456</div></div>
  </div>
  <nav class="main-nav">
    <span style="left:472px">Home</span>
    <span style="left:546px">About us</span>
    <span style="left:634px">Projects</span>
    <span style="left:722px">Equipment</span>
    <span style="left:822px">Activities</span>
    <span style="left:914px">Clients</span>
    <span style="left:994px">Contact us</span>
  </nav>
</header>

<section class="hero">
  <svg class="abs" style="left:0;top:0" width="1200" height="492" viewBox="0 0 1200 492" role="img" aria-label="Photo of an orange excavator on a construction site with tower cranes and a building under construction">
    <defs>
      <linearGradient id="heroSky" x1="0" y1="0" x2="0" y2="1">
        <stop offset="0" stop-color="#3b4a5a"/>
        <stop offset=".45" stop-color="#7d7f7c"/>
        <stop offset=".75" stop-color="#8a6a4c"/>
        <stop offset="1" stop-color="#5a4330"/>
      </linearGradient>
      <linearGradient id="heroShade" x1="0" y1="0" x2="1" y2="0">
        <stop offset="0" stop-color="#000" stop-opacity=".45"/>
        <stop offset=".6" stop-color="#000" stop-opacity=".1"/>
        <stop offset="1" stop-color="#000" stop-opacity="0"/>
      </linearGradient>
    </defs>
    <polygon points="0,0 1200,0 1200,430 0,492" fill="url(#heroSky)"/>
    <polygon points="0,0 1200,0 1200,430 0,492" fill="url(#heroShade)"/>
    <polygon points="0,492 1200,430 1200,492" fill="#fff"/>
  </svg>
  <h1 class="hero-title">EARTHMOVING &amp; CIVIL WORKS</h1>
  <p class="hero-text">Mauris volutpat nulla a enim efficitur elementum porttor at diam aliquam et elit elementum fermentum nisl sed, pellentesque mares. Integer blandit erat bibendum pulvinar lobortis. Mauris sed turpis.</p>
  <div class="btn" style="left:136px;top:284px;width:139px;height:35px">Know more</div>
  <svg class="hero-arrow" style="left:93px" viewBox="0 0 20 20" aria-hidden="true"><path d="M13 4 7 10l6 6" fill="none" stroke="#fff" stroke-width="2"/></svg>
  <svg class="hero-arrow" style="left:1079px" viewBox="0 0 20 20" aria-hidden="true"><path d="M7 4l6 6-6 6" fill="none" stroke="#fff" stroke-width="2"/></svg>
</section>

<h2 class="section-title" style="top:634px">Explore our <em>main services</em></h2>

<div class="service" style="left:115px">
  <div class="service-photo" role="img" aria-label="Photo of a loader tipping a bucket of soil" style="background:radial-gradient(circle at 50% 35%,#dfe6ee,#b69a78 60%,#8a6a48)"></div>
  <h3>Earthworks</h3>
  <p>Surface development for highways, canals, urban developments and more.</p>
</div>
<div class="service" style="left:359px">
  <div class="service-photo" role="img" aria-label="Photo of an underground mining loader in a tunnel" style="background:radial-gradient(circle at 50% 55%,#a27a3c,#4a3a2a 60%,#2a241e)"></div>
  <h3>Underground</h3>
  <p>Water, storm, sewer, and other services.</p>
</div>
<div class="service" style="left:605px">
  <div class="service-photo" role="img" aria-label="Photo of a heavy haul truck with a low loader trailer" style="background:linear-gradient(180deg,#7da5d6,#c8d6e6 45%,#9a8f7e 70%,#6b6b66)"></div>
  <h3>Heavy haul</h3>
  <p>Hauling loads up to 120t through-out Canada and the U.S.</p>
</div>
<div class="service" style="left:850px">
  <div class="service-photo" role="img" aria-label="Photo of a long reach excavator on a grass field" style="background:linear-gradient(180deg,#b9c3cc,#d3d8dc 45%,#9a4a32 60%,#6f8a52 80%)"></div>
  <h3>Specialty</h3>
  <p>Long reach excavators, shovels and more.</p>
</div>

<svg class="abs" style="left:0;top:1050px" width="1200" height="470" viewBox="0 0 1200 470" role="img" aria-label="Orange band with a faint excavator photo in the background">
  <defs>
    <linearGradient id="aboutBand" x1="0" y1="0" x2="1" y2="1">
      <stop offset="0" stop-color="var(--orange-soft)"/>
      <stop offset=".5" stop-color="var(--orange)"/>
      <stop offset="1" stop-color="var(--orange-deep)"/>
    </linearGradient>
  </defs>
  <polygon points="0,44 905,4 1200,30 1200,470 0,440" fill="url(#aboutBand)"/>
</svg>
<div class="about-photo" role="img" aria-label="Photo of an excavator silhouetted against a sunset" style="background:radial-gradient(circle at 45% 45%,#ffd24a,#f08a1a 25%,#6a2e0c 55%,#140a06 80%)"></div>
<h2 class="about-title">About Mosk trail</h2>
<p class="about-text" style="top:1174px">Mauris volutpat nulla a enim efficitur elementum porttor at diam aliquam et elit elementum, fermentum nisl sed, pellentesque mares. Integer blandit erat bibendum pulvinar lobortis. Mauris sed turpis.</p>
<p class="about-text" style="top:1272px">Nulla vitae dui et velit sagittis fermentum. Donec rhoncus tincidunt. Nullam nibh tellus, blandit vel leo vulputate, commodo edmentum. Pellentesque eget quam ultrices, semperos lacus et, lacinia neue. Class aptent taciti sociosqu ad litora torquent per conubia nostra, per inceptos himenaeos. In id accumsan augue. Mauris ultricores, metus quis semper sagittis, tellus lectus pharetra massa, ut ultces.</p>

<svg class="abs" style="left:0;top:1484px;z-index:-1" width="1200" height="660" viewBox="0 0 1200 660" aria-hidden="true"><rect width="1200" height="660" fill="var(--paper)"/></svg>
<h2 class="section-title" style="top:1563px">Our equipment</h2>

<div class="equip" style="left:131px;top:1629px"><div class="equip-photo" role="img" aria-label="Photo of a row of yellow excavators" style="background:linear-gradient(180deg,#dfe6ea,#c7b24a 50%,#9a9a8c)"></div><h4>Excavators</h4></div>
<div class="equip" style="left:452px;top:1629px"><div class="equip-photo" role="img" aria-label="Photo of a motor grader" style="background:linear-gradient(180deg,#6d8fb0,#a89a72 55%,#6f6650)"></div><h4>Graders</h4></div>
<div class="equip" style="left:772px;top:1629px"><div class="equip-photo" role="img" aria-label="Photo of a white skid steer loader on a road verge" style="background:linear-gradient(180deg,#8a8d90,#e6e6e6 45%,#7a8a58 80%)"></div><h4>Bobcats</h4></div>
<div class="equip" style="left:131px;top:1857px"><div class="equip-photo" role="img" aria-label="Photo of a yellow bulldozer pushing rubble" style="background:linear-gradient(180deg,#4a4a48,#b89a3a 50%,#5a5048)"></div><h4>Dozers</h4></div>
<div class="equip" style="left:452px;top:1857px"><div class="equip-photo" role="img" aria-label="Photo of green skip bins on grass" style="background:linear-gradient(180deg,#b8c2c8,#3a6a4a 45%,#4a8a3a)"></div><h4>Skip bins</h4></div>
<div class="equip" style="left:772px;top:1857px"><div class="equip-photo" role="img" aria-label="Photo of a tracked loader with a brush cutter" style="background:linear-gradient(180deg,#a9b1b6,#d8d8d4 45%,#8a7a62)"></div><h4>Bruse cutting</h4></div>

<footer>
  <svg class="abs" style="left:0;top:2106px" width="1200" height="342" viewBox="0 0 1200 342" aria-hidden="true"><polygon points="0,32 900,0 1200,8 1200,342 0,342" fill="var(--footer)"/></svg>
  <div class="footer-col" style="left:146px;width:230px">
    <h4>Get in touch</h4>
    <div class="info-row"><svg class="info-icon" viewBox="0 0 12 16" height="16"><path d="M6 0a6 6 0 0 0-6 6c0 4.5 6 10 6 10s6-5.5 6-10a6 6 0 0 0-6-6zm0 8.5A2.5 2.5 0 1 1 6 3.5a2.5 2.5 0 0 1 0 5z" fill="#fff"/></svg><span>27 Quarry Road, Level 3, Suite 12, Ironbark Park, Northvale / NV - Post 4820</span></div>
    <div class="info-row" style="color:#fff;font-size:13px"><svg class="info-icon" viewBox="0 0 12 12" height="13"><path d="M2 1l2.2 0 1 3-1.4 1a7 7 0 0 0 3.2 3.2l1-1.4 3 1V10a1 1 0 0 1-1 1A9 9 0 0 1 1 2a1 1 0 0 1 1-1z" fill="#fff"/></svg><span>(07) 5550-1842</span></div>
    <div class="info-row"><svg class="info-icon" viewBox="0 0 12 9" height="10"><rect width="12" height="9" fill="#fff"/><path d="M0 0 6 5 12 0" fill="none" stroke="#2a2a2a" stroke-width="1.2"/></svg><span>office@mosktrail.example</span></div>
  </div>
  <div class="footer-col" style="left:411px">
    <h4>Company links</h4>
    <ul class="footer-links"><li>Home</li><li>About us</li><li>Services</li><li>Equipment</li><li>Clients</li><li>About us</li></ul>
  </div>
  <div class="footer-col" style="left:604px">
    <h4>Newsletter signup</h4>
    <p class="newsletter-note">If you want receive our all weekly updates signup below.</p>
    <div class="signup"><div class="signup-field">Email Address</div><div class="signup-btn"><svg width="12" height="12" viewBox="0 0 12 12"><path d="M0 5 12 0 7 12 5.5 6.5z" fill="#fff"/></svg></div></div>
  </div>
  <div class="footer-col" style="left:857px">
    <h4>Social links</h4>
    <div class="social" aria-label="Social network links"><span></span><span></span><span></span><span></span><span></span></div>
  </div>
  <div class="copyright">© Copyright 2018 mosktrail.example. All rights reserved.</div>
</footer>

</body>
</html>
```